Image / graphic for the side of Heating oil Delivery trucks. To display name and brand

We deliver heating oil in the Northeast United States. Most heating oil companies are super boring and I don't want Brookfield Fuel to be like that. Colors we have used in the past are Red / Yellow / black. Our current logo has a retro feel and I would like to try to stay within that category. My idea is to have some sort of basic home image, with the Brookfield Fuel Name next to it under it coming out of the house etc. But I am not set on this design. Want to see options. The Brookfield fuel name needs to be clear as it will be on the side of a moving vehicle. I like these retro stars (shown in this wrap) but can use or not use. I want the graphic to be sharp and clear since the image will be seen for seconds if driving down the road. Not sure if one color or multiple colors would work. I have attached our current logo and the stars that I like from a current truck. But again, not set I don't like the image on the current truck but like the stars.
Look and feel
Each slider illustrates characteristics of the customer's brand and the style your logo design should communicate.

```html
<!DOCTYPE html>
<html lang="en">
<head>
<meta charset="utf-8">
<title>Brookfield Fuel — Truck Side Panel</title>
<link href="https://fonts.googleapis.com/css2?family=Exo+2:wght@800&display=swap" rel="stylesheet">
<style>
  :root {
    --fuel-red: #ec3030;
    --fuel-yellow: #fdd42c;
    --fuel-black: #1c1a19;
    --star-white: #ffffff;
    --page-bg: #ffffff;
  }
  html, body {
    margin: 0;
    padding: 0;
    width: 1200px;
    height: 900px;
    overflow: hidden;
    background: var(--page-bg);
  }
  .canvas {
    position: relative;
    width: 1200px;
    height: 900px;
  }
  .truck-panel {
    position: absolute;
    left: 60px;
    top: 295px;
    width: 1080px;
    height: 311px;
    display: block;
  }
  .panel-bg { fill: var(--fuel-yellow); }
  .panel-band { fill: var(--fuel-red); }
  .brand-dot { fill: var(--fuel-black); }
  .brand-name {
    font-family: "Exo 2", sans-serif;
    font-weight: 800;
    font-size: 60px;
    fill: var(--fuel-black);
  }
  .phone-number {
    font-family: "Exo 2", sans-serif;
    font-weight: 800;
    font-size: 40px;
    letter-spacing: 1px;
    fill: var(--fuel-black);
  }
  .hazmat-outer { fill: var(--fuel-red); }
  .hazmat-inner { fill: none; stroke: var(--star-white); stroke-width: 2.5; }
  .hazmat-label { fill: var(--star-white); stroke: var(--fuel-black); stroke-width: 1.5; }
  .hazmat-number {
    font-family: "Exo 2", sans-serif;
    font-weight: 800;
    font-size: 19px;
    fill: var(--fuel-black);
  }
  .hazmat-class {
    font-family: "Exo 2", sans-serif;
    font-weight: 800;
    font-size: 11px;
    fill: var(--star-white);
  }
  .sparkle { fill: url(#sparkleGlow); }
</style>
</head>
<body>
<div class="canvas">
  <svg class="truck-panel" viewBox="0 0 1080 311" xmlns="http://www.w3.org/2000/svg">
    <defs>
      <radialGradient id="sparkleGlow">
        <stop offset="0" stop-color="#ffffff" stop-opacity="1"/>
        <stop offset="1" stop-color="#ffffff" stop-opacity="0"/>
      </radialGradient>
    </defs>

    <rect class="panel-bg" x="0" y="0" width="1080" height="311"/>
    <polygon class="panel-band" points="0,0 406,0 0,183"/>
    <polygon class="panel-band" points="1080,93 1080,311 639,311"/>

    <g class="sparkles">
      <circle class="sparkle" cx="119" cy="46" r="26" role="img" aria-label="retro sparkle star"/>
      <circle class="sparkle" cx="318" cy="35" r="20" role="img" aria-label="retro sparkle star"/>
      <circle class="sparkle" cx="39" cy="110" r="20" role="img" aria-label="retro sparkle star"/>
      <circle class="sparkle" cx="1029" cy="163" r="28" role="img" aria-label="retro sparkle star"/>
      <circle class="sparkle" cx="789" cy="232" r="36" role="img" aria-label="retro sparkle star"/>
      <circle class="sparkle" cx="973" cy="225" r="20" role="img" aria-label="retro sparkle star"/>
    </g>

    <g class="brand">
      <circle class="brand-dot" cx="150" cy="160" r="60"/>
      <text class="brand-name" x="228" y="182">Brookfield Fuel</text>
    </g>

    <text class="phone-number" x="609" y="114">555.014.2290</text>

    <g class="hazmat-placard" transform="translate(961 70)">
      <rect class="hazmat-outer" x="-32" y="-32" width="64" height="64" transform="rotate(45)"/>
      <rect class="hazmat-inner" x="-27" y="-27" width="54" height="54" transform="rotate(45)"/>
      <rect class="hazmat-label" x="-25" y="-10" width="50" height="20"/>
      <text class="hazmat-number" x="0" y="7" text-anchor="middle">1223</text>
      <text class="hazmat-class" x="0" y="26" text-anchor="middle">3</text>
    </g>
  </svg>
</div>
</body>
</html>
```